Brightmoor Partners Branding Revamp

We are a consulting company, looking for a way to display and promote our brand. We have 2 sides to the business- Brightmoor (financial) and Partners (cyber security). The financial side products relate to business necessities: card processing, website design/hosting/maintenance, VoIP phone systems. The cyber security side promotes a bundled package of 4 solutions: network vulnerability scan, dark web scan, anti-ransomeware/malware software, and image-level backups. We want people to understand that partnering with Brightmoor Partners gives them “Elevated Peace of Mind” (tagline). Current badge and logos uploaded.

Target Market(s)

Small businesses

Contact Information for Business Card

Lena Marwick, Vice President, lena@brightmoorpartners.example, 555-806-1937, www.brightmoorpartners.example

Requirements
Nice to have
• I do prefer the darker background for front and back

```html
<!DOCTYPE html>
<html lang="en">
<head>
<meta charset="utf-8">
<title>Brightmoor Partners – Business Card</title>
<link href="https://fonts.googleapis.com/css2?family=Montserrat:wght@400;500;700&display=swap" rel="stylesheet">
<style>
  :root {
    --bg: #26262b;
    --card-dark: #161618;
    --card-light: #ffffff;
    --red: #e31e26;
    --red-deep: #a8141a;
    --ink: #2a2a2a;
    --white: #ffffff;
  }
  * { box-sizing: border-box; margin: 0; padding: 0; }
  html, body {
    width: 1200px; height: 947px; overflow: hidden;
    background: var(--bg);
    font-family: "Montserrat", Arial, sans-serif;
  }
  .canvas {
    position: relative; width: 1200px; height: 947px;
    display: flex; flex-direction: column; align-items: center; justify-content: center; gap: 70px;
  }
  .card {
    position: relative; width: 600px; height: 343px;
    border-radius: 16px; overflow: hidden;
    box-shadow: 0 18px 40px rgba(0,0,0,.45);
  }
  .card--front {
    background: var(--card-dark);
    display: flex; align-items: center; justify-content: center; gap: 16px;
  }
  .brand-mark { width: 22px; height: 22px; background: var(--red); }
  .brand-name {
    color: var(--white); font-weight: 500; font-size: 30px;
    letter-spacing: 8px; text-transform: uppercase;
  }
  .card--back { background: var(--card-light); }
  .card--back .accent-band {
    position: absolute; left: 0; right: 0; bottom: 0; height: 16px;
    background: linear-gradient(90deg, var(--red-deep), var(--red));
  }
  .back-brand {
    position: absolute; left: 48px; top: 50%; transform: translateY(-50%);
    display: flex; flex-direction: column; align-items: center; gap: 14px;
  }
  .back-brand .brand-dot { width: 96px; height: 96px; border-radius: 50%; background: var(--red); }
  .back-brand .brand-name-small {
    color: var(--red); font-weight: 500; font-size: 13px; letter-spacing: 2px; text-transform: uppercase;
  }
  .contact {
    position: absolute; left: 268px; top: 70px; right: 24px;
  }
  .contact .person { color: var(--red); font-weight: 700; font-size: 25px; text-transform: uppercase; letter-spacing: .5px; }
  .contact .role { color: var(--ink); font-size: 17px; margin-top: 2px; }
  .contact ul { list-style: none; margin-top: 32px; }
  .contact li {
    display: flex; align-items: center; gap: 10px;
    color: var(--ink); font-size: 15px; line-height: 1; margin-bottom: 11px;
  }
  .contact li svg { flex: none; width: 16px; height: 16px; }
</style>
</head>
<body>
<main class="canvas">
  <section class="card card--front" aria-label="Card front">
    <span class="brand-mark"></span>
    <span class="brand-name">Brightmoor Partners</span>
  </section>

  <section class="card card--back" aria-label="Card back">
    <div class="back-brand">
      <span class="brand-dot"></span>
      <span class="brand-name-small">Brightmoor Partners</span>
    </div>
    <div class="contact">
      <p class="person">Lena Marwick</p>
      <p class="role">Vice President</p>
      <ul>
        <li>
          <svg viewBox="0 0 16 16"><circle cx="8" cy="8" r="8" fill="#e31e26"/><path d="M5.2 4.2l1.4 1.6-.7 1a5 5 0 0 0 2.4 2.4l1-.7 1.6 1.4-.8 1.3c-3 0-6.2-3.2-6.2-6.2z" fill="#fff"/></svg>
          555-806-1937
        </li>
        <li>
          <svg viewBox="0 0 16 16"><circle cx="8" cy="8" r="8" fill="#e31e26"/><rect x="4" y="5" width="8" height="6" fill="#fff"/><path d="M4 5l4 3.2L12 5" fill="none" stroke="#e31e26" stroke-width="1"/></svg>
          lena@brightmoorpartners.example
        </li>
        <li>
          <svg viewBox="0 0 16 16"><circle cx="8" cy="8" r="8" fill="#e31e26"/><circle cx="8" cy="8" r="4.2" fill="none" stroke="#fff" stroke-width="1"/><path d="M3.8 8h8.4M8 3.8c-2 2.4-2 6 0 8.4M8 3.8c2 2.4 2 6 0 8.4" fill="none" stroke="#fff" stroke-width="1"/></svg>
          www.brightmoorpartners.example
        </li>
      </ul>
    </div>
    <div class="accent-band"></div>
  </section>
</main>
</body>
</html>
```